Flyer Design

we are cleaning company specialize in home cleaning, based in North Shore in Auckland (NZ).
Company name PM is initial of pure mint.
we provide professional, high standard,attention to detail service,
to make dust-free, sparkling house and no-stress family.

(business practice)--don't write this title
"colour coded cleaning system"
---we use different colour's microfiber cloths and mop heads for more hygene.
"green and clean"
---we use eco-friendly, non-toxic cleaning products for environment and your family's health.

service we offer
regular cleaning service
--weekly, fortnightly, monthly
one-off cleaning service
---move in/out cleaning
---rental inspection cleaning
---spring cleaning
---open home cleaning
---remodeling clean-up
---special occasion cleaning(event,party)

special cleaning
---window cleaning
---oven cleaning
---house washing(water blasting)

Free in home no obligation consultation and 50% off first service.
contact no; Rob and Helen 021 0847 5526,09-571-6842
e-mail info@pmhomecare.example.nz
www.pmhomecare.example.nz

we would like to see designs that use colours blue and lite pink, clean, bright and friendly image.

Target Market(s)

Woman aged between late 30th to 60th, housewives, career woman, senior etc.

Industry/Entity Type

Environment

Requirements
Should not have
• For the introduction instead of writing what I have written above verbatim, would you be able to go to our website and paraphrase/reword the introduction that's already there?

Also please don't use the picture on the website, we are planning to change the picture. Thanks.

```html
<!DOCTYPE html>
<html lang="en">
<head>
<meta charset="utf-8">
<title>PM Cleaning Service – Flyer</title>
<link href="https://fonts.googleapis.com/css2?family=Archivo+Black&family=Arimo:wght@400;700&display=swap" rel="stylesheet">
<style>
:root{
  --pink:#e8479a;
  --pink-soft:#f7a8cf;
  --pink-pale:#fbd3e6;
  --sky:#2fb4ec;
  --sky-light:#8fdcf7;
  --sky-deep:#1590d4;
  --navy:#1d3f93;
  --ink:#111;
  --white:#fff;
  --page:#ecebe8;
}
*{box-sizing:border-box;margin:0;padding:0}
html,body{width:927px;height:1200px;overflow:hidden;background:var(--page)}
body{position:relative;font-family:"Arimo",Arial,sans-serif;font-weight:700}
.flyer{position:absolute;left:93px;width:741px;height:522px;overflow:hidden;
  background:linear-gradient(135deg,var(--sky-light) 0%,var(--sky) 45%,var(--sky-deep) 100%);
  box-shadow:0 4px 14px rgba(0,0,0,.25)}
.flyer--front{top:64px}
.flyer--back{top:606px}
.flyer svg.backdrop{position:absolute;inset:0;width:100%;height:100%}
.abs{position:absolute}
.photo{position:absolute;border:4px solid var(--white);box-shadow:0 2px 6px rgba(0,0,0,.3)}

/* front */
.front-title{left:24px;top:6px;font-family:"Archivo Black",sans-serif;font-size:22px;color:var(--white);
  text-shadow:1px 1px 0 #333,-1px 1px 0 #333,1px -1px 0 #333,-1px -1px 0 #333}
.intro{left:16px;top:68px;width:395px;font-size:10px;line-height:1.3;color:var(--white)}
.sub-heading{font-family:"Archivo Black",sans-serif;color:var(--pink);font-size:15px;
  text-shadow:1px 1px 0 var(--white),-1px -1px 0 var(--white),1px -1px 0 var(--white),-1px 1px 0 var(--white)}
.team-heading{left:16px;top:133px}
.bullets{list-style:none;font-size:9px;line-height:1.25;color:var(--ink)}
.bullets li{position:relative;padding-left:11px}
.bullets li::before{content:"";position:absolute;left:1px;top:3px;width:6px;height:6px;border-radius:50%;background:var(--ink)}
.team-points{left:16px;top:157px;width:400px}
.colour-heading{left:304px;top:258px}
.colour-points{left:298px;top:280px;width:385px}
.colour-key{left:298px;top:334px;width:182px;font-size:9px;line-height:1.25;color:var(--ink)}
.collage{left:420px;top:50px;width:282px;height:160px;background:linear-gradient(135deg,#d9dde2,#8a7a6d 50%,#c7d6e3)}
.couple{left:0;top:250px;width:292px;height:272px;border:none;box-shadow:none;
  background:linear-gradient(180deg,#f4c9dd,#fbeef4 40%,#5fa6de 80%,#2f74c0)}
.cloths{left:486px;top:330px;width:236px;height:150px;background:linear-gradient(135deg,#c9d6e0,#e6c4a6 55%,#b8c7cc)}
.caption{left:380px;top:488px;width:360px;text-align:center;font-size:9.5px;color:var(--white);line-height:1.3}

/* back */
.back-title{right:26px;top:12px;font-family:"Archivo Black",sans-serif;font-size:26px;color:var(--white);letter-spacing:.5px}
.back-intro{left:34px;top:76px;width:500px;font-size:12.5px;line-height:1.32;color:var(--ink)}
.services-heading{left:28px;top:190px;font-size:21px}
.special-heading{left:28px;top:410px;font-size:21px}
.service-list{list-style:none;font-size:14px;line-height:21px;color:var(--ink)}
.regular{left:28px;top:215px}
.special{left:28px;top:435px}
.offer{left:318px;top:206px;width:405px;text-align:center;font-family:"Archivo Black",sans-serif;color:var(--pink);line-height:1.25;
  text-shadow:1px 1px 0 var(--white),-1px -1px 0 var(--white),1px -1px 0 var(--white),-1px 1px 0 var(--white)}
.offer .big{color:var(--navy);font-size:24px}
.offer .line{font-size:16px;display:block}
.offer .contact{font-size:17px;margin-top:10px}
.offer .phones{color:var(--navy);font-size:17px;letter-spacing:.5px}
.vacuum{left:472px;top:380px;width:269px;height:142px;border:none;box-shadow:none;
  background:linear-gradient(160deg,rgba(255,255,255,0) 0%,rgba(150,175,200,.7) 50%,rgba(90,105,125,.8) 100%)}
.web{left:280px;top:452px;width:440px;text-align:right;font-family:"Archivo Black",sans-serif;font-size:15.5px;line-height:1.4;color:var(--navy);
  text-shadow:1px 1px 0 var(--white),-1px -1px 0 var(--white),1px -1px 0 var(--white),-1px 1px 0 var(--white)}
</style>
</head>
<body>

<section class="flyer flyer--front">
  <svg class="backdrop" viewBox="0 0 741 522" aria-hidden="true">
    <rect x="0" y="0" width="741" height="40" fill="var(--pink)"/>
    <path d="M0 40 L741 40 L741 48 Q380 62 0 46 Z" fill="var(--white)"/>
    <path d="M300 522 Q330 380 470 290 Q600 220 741 250 L741 300 Q600 270 500 330 Q380 410 360 522 Z" fill="var(--white)"/>
    <path d="M360 522 Q380 410 500 330 Q600 270 741 300 L741 522 Z" fill="var(--pink)"/>
    <path d="M0 240 Q150 230 300 522 L0 522 Z" fill="var(--pink-soft)" opacity=".35"/>
    <g fill="var(--pink-pale)">
      <circle cx="720" cy="232" r="13"/><circle cx="728" cy="262" r="8"/>
      <circle cx="250" cy="232" r="8"/><circle cx="395" cy="470" r="20"/>
      <circle cx="445" cy="445" r="10"/><circle cx="370" cy="425" r="8"/>
      <circle cx="275" cy="92" r="7"/><circle cx="245" cy="120" r="5"/>
    </g>
  </svg>
  <h1 class="abs front-title">The Hale's Special Home Cleaning Services:</h1>
  <p class="abs intro">We strive to provide a professional, high quality home cleaning services at an affordable price. we do our best to meet every customers requirement whatever your personal cleaning needs are. Because we always aim to make your home sparkle clean and healthy place to live. we love the job!</p>
  <h2 class="abs sub-heading team-heading">Husband &amp; wife team</h2>
  <ul class="abs bullets team-points">
    <li>Dependable, friendly and honest</li>
    <li>Our way of cleaning: High standard; Attention to detail; 100% satisfaction guarantee</li>
    <li>From bedrooms, kitchen, bathrooms to window sills, window frame, skirting board we provide high quality services and satisfaction Guarantee</li>
    <li>We carry all necessary equipment and try to use eco-friendly, non-toxic cleaning products where possible for your family's health and environment.</li>
    <li>Free in-home no obligation quote and reference available.</li>
  </ul>
  <div class="photo collage" role="img" aria-label="Collage of cleaning photos: vacuum, bedroom, bathroom and gloved hand wiping a window"></div>
  <h2 class="abs sub-heading colour-heading">Colour coded cleaning system:</h2>
  <ul class="abs bullets colour-points">
    <li>To improve hygiene and reduce the risk of cross-contamination during the cleaning process,</li>
    <li>We use different coloured microfibre cloths and mop head for different area of the home.</li>
  </ul>
  <p class="abs colour-key">Red: bathrooms, shower, basins<br>Blue: kitchen, dining room<br>Green: wiping of furniture surface, decoration, ornament, vase, pictures<br>Disposable wipes only: toilets</p>
  <div class="photo couple" role="img" aria-label="Portrait photo of the husband and wife cleaning team"></div>
  <div class="photo cloths" role="img" aria-label="Photo of stacked coloured microfibre cloths and spray bottles"></div>
  <p class="abs caption">Cloths: different coloured microfibre cloths<br>for different area / Cleaning product: eco- friendly</p>
</section>

<section class="flyer flyer--back">
  <svg class="backdrop" viewBox="0 0 741 522" aria-hidden="true">
    <path d="M0 0 L741 0 L741 60 Q370 48 0 58 Z" fill="var(--pink)"/>
    <path d="M0 58 Q370 48 741 60 L741 68 Q370 58 0 68 Z" fill="var(--white)"/>
    <path d="M0 395 Q200 420 300 522 L0 522 Z" fill="var(--pink)"/>
    <path d="M380 522 Q430 330 620 250 Q690 225 741 228 L741 260 Q640 270 540 340 Q460 410 430 522 Z" fill="var(--white)"/>
    <path d="M430 522 Q460 410 540 340 Q640 270 741 260 L741 522 Z" fill="var(--pink)" opacity=".85"/>
    <g fill="var(--pink-pale)">
      <circle cx="590" cy="112" r="30"/><circle cx="655" cy="92" r="13"/>
      <circle cx="692" cy="150" r="9"/><circle cx="300" cy="448" r="24"/>
      <circle cx="358" cy="470" r="11"/><circle cx="305" cy="310" r="9"/>
      <circle cx="258" cy="355" r="7"/><circle cx="620" cy="175" r="8"/>
    </g>
  </svg>
  <h1 class="abs back-title">PM CLEANING SERVICE</h1>
  <p class="abs back-intro">We provide high quality services and satisfaction Guarantee.<br>We carry all necessary equipment and try to use eco-friendly,<br>non-toxic cleaning products where possible for your family's health<br>and environment.<br>Free in-home no obligation quote and reference available.</p>
  <h2 class="abs sub-heading services-heading">Services we provide:</h2>
  <ul class="abs service-list regular">
    <li>Regular cleaning service</li>
    <li>Weekly, fortnightly, monthly</li>
    <li>One-off cleaning service</li>
    <li>Move in/out cleaning</li>
    <li>Rental inspection cleaning</li>
    <li>Spring cleaning</li>
    <li>Open home cleaning</li>
    <li>Remodeling clean-up</li>
    <li>Special occasion cleaning(event,party)</li>
  </ul>
  <h2 class="abs sub-heading special-heading">Special cleaning:</h2>
  <ul class="abs service-list special">
    <li>Window cleaning</li>
    <li>Oven cleaning</li>
    <li>House washing(water blasting)</li>
  </ul>
  <div class="photo vacuum" role="img" aria-label="Photo of a vacuum cleaner head on carpet"></div>
  <div class="abs offer">
    <span class="line"><span class="big">FREE</span> IN HOME NO OBLIGATION</span>
    <span class="line">CONSULTATION AND</span>
    <span class="line" style="margin-top:8px"><span class="big">50%</span> OFF FIRST SERVICE</span>
    <span class="line contact">CONTACT# ROB &amp; HELEN</span>
    <span class="line phones">021 0847 5526 / 09-571-6842</span>
  </div>
  <p class="abs web">e-mail:info@pmhomecare.example.nz<br>Website: www.pmhomecare.example.nz</p>
</section>

</body>
</html>
```